Vesker Wine Label

We are seeking a wine label. Clean, minimalist, pen & ink art. We already make meads and ciders, (labels online have not all been updated- bottom few have) which have a craft feel, but now would like a simple wine label for our new line of wines. We have all the necessary verbage already required for wine labels. We just need room on the sides (will use one large label) to print the description of our business, govt. warnings, etc. We would like to use our last name - Vesker- with some simple pen and ink art in the upper right hand corner of a bumble bee with some botanical somethings. We make all of our products on a working farm with bees, and our farm logo is a bumble bee...so it's just a little tie in there. We will keep all the labels the same apart from the varietal, vintage, and appellation (in some cases). Label inspiration is something like Soliv. Preferably printing on cream colored label paper. First wine to be bottled is a black Spanish Rose. Thank you for your consideration and your time.

35 -60 demo. red wine drinkers

French Winery

• pen and ink art

```html
<!DOCTYPE html>
<html lang="en">
<head>
<meta charset="utf-8">
<title>Vesker Rosé Label</title>
<link rel="stylesheet" href="https://fonts.googleapis.com/css2?family=Playfair+Display:wght@400&display=swap">
<style>
  :root {
    --backdrop: #eeeeee;
    --label-cream: #f3efd9;
    --brand-magenta: #9c1463;
    --rose-pink: #e0307a;
    --berry-deep: #7a1650;
    --berry-light: #c7458e;
  }
  * { margin: 0; padding: 0; box-sizing: border-box; }
  html, body {
    width: 1200px;
    height: 1199px;
    overflow: hidden;
    background: var(--backdrop);
  }
  .canvas {
    position: relative;
    width: 1200px;
    height: 1199px;
  }
  .wine-label {
    position: absolute;
    left: 380px;
    top: 80px;
    width: 440px;
    height: 1040px;
    background: var(--label-cream);
    font-family: "Playfair Display", Georgia, serif;
  }
  .brand-name {
    position: absolute;
    left: 0;
    width: 420px;
    top: 150px;
    text-align: center;
    font-size: 92px;
    font-weight: 400;
    line-height: 1;
    color: var(--brand-magenta);
  }
  .varietal {
    position: absolute;
    right: 70px;
    top: 272px;
    font-size: 40px;
    line-height: 1;
    color: var(--rose-pink);
  }
  .bottle-art {
    position: absolute;
    left: 156px;
    top: 414px;
    width: 138px;
    height: 626px;
  }
  .bottle-art .base-band {
    position: absolute;
    left: 4px;
    bottom: 0;
    width: 124px;
    height: 124px;
    background: var(--brand-magenta);
  }
  .spec {
    position: absolute;
    top: 930px;
    font-size: 24px;
    letter-spacing: 2px;
    color: var(--brand-magenta);
    text-transform: uppercase;
  }
  .spec--volume { left: 8px; }
  .spec--abv { right: 8px; }
</style>
</head>
<body>
  <main class="canvas">
    <section class="wine-label">
      <h1 class="brand-name">Vesker</h1>
      <p class="varietal">Rosé</p>

      <div class="bottle-art">
        <svg width="138" height="502" viewBox="0 0 138 502" role="img" aria-label="Illustration of a wine bottle formed from clusters of pink grape bubbles">
          <defs>
            <linearGradient id="berryFade" x1="0" y1="0" x2="0" y2="1">
              <stop offset="0" stop-color="var(--berry-light)" stop-opacity="0.55"/>
              <stop offset="1" stop-color="var(--berry-deep)"/>
            </linearGradient>
          </defs>
          <rect x="0" y="0" width="138" height="502" fill="url(#berryFade)"/>
        </svg>
        <div class="base-band"></div>
      </div>

      <p class="spec spec--volume">750 ml.</p>
      <p class="spec spec--abv">Alc 11.5%</p>
    </section>
  </main>
</body>
</html>
```